Professional Flyer - for Brindle Vale

Create a professional looking flyer than the one attached.
Change headline to: Hemp Homes the next Evolution in Green Building
Sub headline: Sustainable, Durable and Healthier to Live in
Delete the address below the headline.
Use as much as the other information that makes sense and that you have room for.

Thanks!

```html
<!DOCTYPE html>
<html lang="en">
<head>
<meta charset="utf-8">
<title>Hemp Homes – Brindle Vale Builders</title>
<link rel="stylesheet" href="https://fonts.googleapis.com/css2?family=Anton&family=Roboto+Condensed:wght@300;400;700&display=swap">
<style>
  :root {
    --forest: #1d5a22;
    --forest-deep: #154a1a;
    --headline-green: #1f6a2a;
    --lemon: #f3ee1c;
    --sky-top: #f4f7f8;
    --sky-bottom: #dfe8ec;
    --white: #ffffff;
  }
  * { margin: 0; padding: 0; box-sizing: border-box; }
  html, body { width: 849px; height: 1200px; overflow: hidden; }
  body { font-family: "Roboto Condensed", "Arial Narrow", sans-serif; }

  .flyer {
    position: relative;
    width: 849px;
    height: 1200px;
    overflow: hidden;
    background: linear-gradient(var(--sky-top), var(--sky-bottom) 520px, var(--forest) 520px, var(--forest-deep));
  }

  .headline {
    position: absolute;
    top: 4px; left: 0; width: 849px;
    text-align: center;
    font-family: "Anton", "Impact", sans-serif;
    font-size: 128px;
    line-height: 1.05;
    letter-spacing: 3px;
    color: var(--headline-green);
    -webkit-text-stroke: 4px var(--lemon);
    paint-order: stroke fill;
  }
  .subheadline {
    position: absolute;
    top: 136px; left: 0; width: 849px;
    text-align: center;
    font-family: "Anton", "Impact", sans-serif;
    font-size: 40px;
    line-height: 1.2;
    letter-spacing: 0.5px;
    color: var(--lemon);
    -webkit-text-stroke: 5px var(--forest-deep);
    paint-order: stroke fill;
  }

  .home-rendering {
    position: absolute;
    top: 188px; left: 60px;
    width: 740px; height: 335px;
    background: radial-gradient(ellipse at 50% 45%, #c9a671 0%, #8a6a4a 38%, #7c9a6a 62%, rgba(223,232,236,0) 78%);
  }

  .band {
    position: absolute; left: 0; width: 849px;
    background: var(--lemon);
    color: var(--forest);
  }
  .tagline-band {
    top: 523px; height: 46px;
    text-align: center;
    font-size: 32px;
    line-height: 46px;
  }

  .features-frame {
    position: absolute;
    top: 638px; left: 38px;
    width: 773px; height: 295px;
    border: 3px solid var(--lemon);
    border-radius: 6px;
  }
  .material-title {
    position: absolute;
    top: 587px; left: 108px;
    width: 632px; height: 78px;
    background: var(--forest);
    border: 3px solid var(--lemon);
    border-radius: 8px;
    color: var(--lemon);
    font-weight: 700;
    font-size: 35px;
    line-height: 35px;
    text-align: center;
    padding-top: 3px;
  }
  .feature-list {
    position: absolute;
    list-style: none;
    color: var(--white);
    font-weight: 300;
    font-size: 27px;
    line-height: 36.8px;
  }
  .feature-list.left { top: 698px; left: 58px; }
  .feature-list.right { top: 715px; left: 439px; }

  .worldwide {
    position: absolute;
    top: 918px; left: 0; width: 849px;
    text-align: center;
  }
  .worldwide span {
    background: var(--forest);
    padding: 0 8px;
    color: var(--lemon);
    font-weight: 700;
    font-size: 24px;
    line-height: 28px;
  }

  .offer {
    position: absolute;
    top: 956px; left: 0; width: 849px;
    text-align: center;
    color: var(--white);
    font-weight: 700;
    font-size: 19.5px;
    line-height: 18.8px;
  }

  .contact-band {
    top: 1127px; height: 44px;
    display: flex;
    justify-content: space-between;
    padding: 0 36px 0 38px;
    font-size: 38px;
    line-height: 44px;
    font-weight: 400;
    letter-spacing: 0.5px;
  }
</style>
</head>
<body>
<main class="flyer">
  <h1 class="headline">HEMP HOMES</h1>
  <h2 class="subheadline">THE NEXT EVOLUTION IN GREEN BUILDING</h2>

  <div class="home-rendering" role="img" aria-label="Illustration of a two-storey craftsman hemp home with a covered porch, solar panels on the roof and trees around it"></div>

  <p class="band tagline-band">SUSTAINABLE, DURABLE AND HEALTHIER TO LIVE IN</p>

  <div class="features-frame"></div>
  <h3 class="material-title">HEMPCRETE IS A NON-STRUCTURAL<br>INSULATION WALL MATERIAL</h3>

  <ul class="feature-list left">
    <li>-HIGH THERMAL INSULATION</li>
    <li>-HIGH SOUND INSULATION</li>
    <li>-HIGH THERMAL INERTIA</li>
    <li>-GOOD VAPOR PERMEABILITY</li>
    <li>-GOOD FLEXIBILITY</li>
    <li>-FIRE RESISTANT</li>
  </ul>
  <ul class="feature-list right">
    <li>-PEST RESISTANT</li>
    <li>-CAN REDUCE CO-2 EMISSIONS</li>
    <li>-CUT ENERGY BILLS BY 50-75%</li>
    <li>-UP TO R-50 WALL INSULATION</li>
    <li>-MOLD RESISTANT</li>
  </ul>

  <p class="worldwide"><span>USED WORLDWIDE</span></p>

  <p class="offer">
    SELLER IS OFFERING THIS BUILD JOB AS A 1200 SQ. FT 3 BR.-2BAW/400 SQ FT<br>
    GARAGE ON 3 ACRES ON BLACKTOP NEAR ASHFORD!<br>
    THIS PLAN WILL OFFER A SOLAR UNIT AS WELL TO REDUCE ENERGY COSTS! AN HOME<br>
    WILL HAVE GEO THERMAL &amp; LED PACKAGE!<br>
    REDUCE YOUR MONTHLY UTILITY BILLS TO BUDGET FRIENDLY $$'S!<br>
    AND... UP TO $15,000 TAX CREDIT!<br>
    UPGRADED W/GEO THERMAL &amp; LED $219,900K
  </p>

  <footer class="band contact-band">
    <span class="company">BRINDLE VALE BUILDERS</span>
    <span class="phone">555-014-2270</span>
  </footer>
</main>
</body>
</html>
```